Retractable banner.
Health Check For Pets
Check for Ear Mites
Skin Health
Fleas & Ticks

A space SERVE BY <NAME OF CLINIC>

Ideally contain pictures of cats and dogs

```html
<!DOCTYPE html>
<html lang="en">
<head>
<meta charset="UTF-8">
<title>Health Check For Pets – Roll-up Banner</title>
<link rel="stylesheet" href="https://fonts.googleapis.com/css2?family=Montserrat:wght@700;800;900&display=swap">
<style>
  :root {
    --ink-dark: #333436;
    --brand-red: #b3131b;
    --banner-top: #f7f7f9;
    --banner-bottom: #e8e8eb;
    --ring: #4a4a4c;
    --white: #ffffff;
    --mite-tone: #efe3b0;
    --dog-tone: #a9c4ee;
    --tick-tone: #8a4a28;
  }
  * { margin: 0; padding: 0; box-sizing: border-box; }
  html, body { width: 768px; height: 1200px; overflow: hidden; }
  body { font-family: "Montserrat", sans-serif; background: var(--banner-bottom); }

  .banner {
    position: relative;
    width: 768px;
    height: 1200px;
    background: linear-gradient(180deg, var(--banner-top) 0%, var(--banner-bottom) 100%);
    overflow: hidden;
  }

  /* Header band */
  .banner-header {
    position: absolute; top: 0; left: 0; width: 100%; height: 102px;
    background: var(--ink-dark); color: var(--white); text-align: center;
  }
  .serve-label {
    position: absolute; top: 26px; left: 54px; right: 54px;
    display: flex; align-items: center; gap: 10px;
    font-weight: 800; font-size: 18px; letter-spacing: 1px; line-height: 1;
  }
  .serve-label::before, .serve-label::after {
    content: ""; flex: 1; height: 2px; background: var(--white);
  }
  .clinic-name {
    position: absolute; top: 46px; left: 0; width: 100%;
    font-weight: 800; font-size: 44px; line-height: 1; letter-spacing: 0.5px;
  }

  /* Headline */
  .headline { position: absolute; top: 0; left: 0; width: 100%; height: 360px; color: var(--brand-red); font-weight: 900; }
  .headline span { position: absolute; left: 0; width: 100%; text-align: center; line-height: 1; letter-spacing: 2px; }
  .headline-health { top: 123px; font-size: 80px; }
  .headline-check { top: 183px; font-size: 120px; }
  .headline-pets { top: 289px; font-size: 64px; }
  .check-tick { position: absolute; left: 575px; top: 171px; width: 115px; height: 82px; }

  /* Checklist */
  .checklist-lines { position: absolute; top: 0; left: 0; width: 768px; height: 1200px; pointer-events: none; }
  .check-item-icon {
    position: absolute; width: 150px; height: 150px; border-radius: 50%;
    border: 4px solid var(--ring); background: var(--white);
    display: flex; align-items: center; justify-content: center;
  }
  .icon-art { width: 96px; height: 96px; border-radius: 50%; }
  .icon-mite { left: 163px; top: 370px; }
  .icon-mite .icon-art { background: radial-gradient(circle, var(--mite-tone) 0%, #f6f0d6 70%, var(--white) 100%); }
  .icon-dog { left: 459px; top: 538px; }
  .icon-dog .icon-art { background: radial-gradient(circle, var(--dog-tone) 0%, #d7e3f7 70%, var(--white) 100%); }
  .icon-tick { left: 163px; top: 706px; }
  .icon-tick .icon-art { background: radial-gradient(circle, var(--tick-tone) 0%, #c79a7e 65%, var(--white) 100%); }

  .check-item-label {
    position: absolute; width: 300px; text-align: center;
    color: var(--brand-red); font-weight: 900; font-size: 48px; line-height: 1.08; letter-spacing: 1px;
  }
  .label-mites { left: 385px; top: 391px; }
  .label-skin { left: 88px; top: 557px; }
  .label-fleas { left: 385px; top: 724px; }

  /* Pets photo */
  .pets-photo {
    position: absolute; left: 0; bottom: 0; width: 100%; height: 334px;
    background:
      radial-gradient(ellipse 34% 50% at 34% 60%, #ecd3a6 0%, #e3c592 45%, rgba(232,232,235,0) 100%),
      radial-gradient(ellipse 20% 60% at 74% 50%, #8b7d70 0%, #6c5f55 45%, rgba(232,232,235,0) 100%),
      linear-gradient(180deg, var(--banner-top), var(--banner-bottom));
  }
</style>
</head>
<body>
  <main class="banner">
    <header class="banner-header">
      <div class="serve-label">SERVE BY:</div>
      <div class="clinic-name">Willow Lane Pet CLINIC</div>
    </header>

    <h1 class="headline">
      <span class="headline-health">HEALTH</span>
      <span class="headline-check">CHECK</span>
      <span class="headline-pets">FOR PETS</span>
    </h1>
    <svg class="check-tick" viewBox="0 0 120 90" aria-hidden="true">
      <path d="M6 52 L22 40 L44 64 L108 4 L116 14 L44 86 Z" fill="var(--brand-red)" transform="translate(-3 4)"/>
      <path d="M6 52 L22 40 L44 64 L108 4 L116 14 L44 86 Z" fill="#111"/>
    </svg>

    <svg class="checklist-lines" viewBox="0 0 768 1200" aria-hidden="true">
      <polyline points="238,520 238,548 461,548" fill="none" stroke="var(--brand-red)" stroke-width="5"/>
      <polyline points="461,677 238,677 238,708" fill="none" stroke="var(--brand-red)" stroke-width="5"/>
    </svg>

    <div class="check-item-icon icon-mite"><div class="icon-art" role="img" aria-label="Illustration of an ear mite"></div></div>
    <div class="check-item-label label-mites">EAR<br>MITES</div>

    <div class="check-item-icon icon-dog"><div class="icon-art" role="img" aria-label="Illustration of a sitting dog with a skin spot"></div></div>
    <div class="check-item-label label-skin">SKIN<br>HEALTH</div>

    <div class="check-item-icon icon-tick"><div class="icon-art" role="img" aria-label="Illustration of a tick"></div></div>
    <div class="check-item-label label-fleas">FLEAS<br>&amp; TICKS</div>

    <div class="pets-photo" role="img" aria-label="Photo of a golden retriever puppy lying beside a tabby kitten"></div>
  </main>
</body>
</html>
```